Brand refresh of quote, work docket and Fire certificate documents

I would like a refresh of our document suit including

1. Front page called VANTO3 Proposal
2. Quote document template
3. Work docket template
4. Fire certificate template - to look like a professional complaint certificate

Examples of documents are attached.

```html
<!DOCTYPE html>
<html lang="en">
<head>
<meta charset="utf-8">
<title>VANTO3 Document Suite</title>
<link rel="stylesheet" href="https://fonts.googleapis.com/css2?family=Oswald:wght@300;600&family=Montserrat:wght@400;500;600;700&family=Open+Sans:wght@400;600;700&display=swap">
<style>
:root{
  --red:#d21f32;
  --orange:#f7941d;
  --orange-deep:#ef6a23;
  --ink:#3a3a3c;
  --muted:#555;
  --panel:#f1f1f3;
  --ghost:#ececec;
  --stage:#e6e6e6;
}
*{box-sizing:border-box;margin:0;padding:0}
html,body{width:1200px;height:1200px;overflow:hidden;background:var(--stage)}
body{position:relative;font-family:"Montserrat",sans-serif;color:var(--ink)}
.page{position:absolute;width:396px;height:511px;background:#fff;overflow:hidden;box-shadow:0 6px 18px rgba(0,0,0,.18)}
.page--cover{left:192px;top:78px}
.page--quote{left:612px;top:78px}
.page--docket{left:192px;top:612px}
.page--cert{left:612px;top:612px}
.abs{position:absolute;white-space:nowrap}

/* brand */
.brand{position:absolute;left:27px;top:34px}
.brand__name{font-family:"Montserrat",sans-serif;font-weight:700;font-size:28px;line-height:1;color:var(--ink);letter-spacing:-.5px}
.brand__tag{font-size:4.3px;letter-spacing:2.2px;color:var(--ink);margin-top:3px}
.company{position:absolute;right:28px;top:26px;text-align:right}
.company__name{font-weight:700;font-size:8.8px;margin-bottom:6px}
.company__line{font-size:6px;line-height:7.8px;color:var(--muted)}
.rule{position:absolute;left:27px;right:28px;top:82px;height:1px;background:#777}
.ghost-word{position:absolute;right:-14px;bottom:-6px;font-family:"Oswald",sans-serif;font-weight:600;font-size:118px;color:var(--ghost);transform:rotate(-90deg);transform-origin:right bottom;line-height:1;white-space:nowrap;translate:0 -100px}
.url-pill{position:absolute;left:34px;top:490px;height:10px;padding:0 6px;border-radius:6px;background:linear-gradient(90deg,var(--red),var(--orange-deep));color:#fff;font-size:5px;line-height:10px;font-weight:600}

/* cover */
.cover__brand{position:absolute;left:0;right:0;top:30px;text-align:center}
.cover__brand .brand__name{font-size:32px}
.cover__brand .brand__tag{font-size:4.6px;letter-spacing:2.6px}
.cover__title{position:absolute;left:0;right:0;top:96px;text-align:center;font-family:"Oswald",sans-serif;font-weight:600;font-size:104px;line-height:1;color:var(--orange);letter-spacing:-1px}
.cover__sub{position:absolute;left:0;right:0;top:204px;text-align:center;font-family:"Oswald",sans-serif;font-weight:300;font-size:62px;line-height:1;color:var(--ink)}
.cover__pill{position:absolute;left:86px;width:222px;top:269px;height:19px;border-radius:10px;background:var(--red);color:#fff;font-size:11.5px;text-align:center;line-height:19px}
.cover__art{position:absolute;left:0;top:300px;width:396px;height:200px}
.cover__band{position:absolute;left:0;bottom:0;width:100%;height:12px;background:linear-gradient(90deg,var(--red),var(--orange));color:#fff;font-size:6.5px;font-weight:700;text-align:center;line-height:12px}

/* quote */
.qtable__head{position:absolute;left:24px;width:347px;top:113px;height:20px;border-radius:6px;background:var(--red);color:#fff;font-size:8.6px;font-weight:600;letter-spacing:.5px}
.qtable__head span,.qrow span{position:absolute;top:0}
.qtable__head span{line-height:20px}
.qtable__body{position:absolute;left:24px;width:347px;top:133px;height:178px;background:var(--panel);border-radius:0 0 8px 8px}
.qrow{position:absolute;left:3px;width:335px;height:40px;border-bottom:1px solid #bdbdbd;font-size:7.8px;letter-spacing:.4px}
.qrow span{line-height:40px}
.c-sl{left:9px}.c-desc{left:35px}.c-price{left:198px}.c-qty{left:255px}.c-total{left:294px}
.qtable__head .c-sl{left:9px}.qtable__head .c-desc{left:35px}.qtable__head .c-price{left:197px}.qtable__head .c-qty{left:253px}.qtable__head .c-total{left:292px}
.q-thanks{left:33px;top:339px;font-size:7.4px;font-weight:700;letter-spacing:.4px}
.q-label-orange{color:var(--orange-deep);font-weight:600;letter-spacing:.5px}
.q-pay{left:33px;top:363px;font-size:8.4px}
.q-paygrid{position:absolute;left:33px;top:377px;font-size:4.4px;line-height:7.4px;font-weight:600}
.q-paygrid b{display:inline-block;width:45px;font-weight:600}
.q-line{position:absolute;left:33px;width:73px;top:418px;height:1px;background:#333}
.q-terms{left:33px;top:428px;font-size:7px}
.q-terms-text{position:absolute;left:33px;top:440px;width:158px;font-size:4px;line-height:6.6px;font-weight:600;white-space:normal}
.q-sum{position:absolute;left:262px;width:92px;font-size:7.2px;font-weight:700;letter-spacing:.4px}
.q-sum span{float:right}
.q-sum--total{font-size:9.8px;font-weight:500;color:var(--orange-deep)}
.q-sign-line{position:absolute;left:282px;width:72px;top:446px;height:1px;background:#333}
.q-sign{left:286px;top:451px;font-size:6.4px;font-weight:700;letter-spacing:.4px}

/* docket */
.dk-title{left:32px;top:97px;font-size:15px;font-weight:700;color:var(--red)}
.dk-date{right:28px;top:105px;font-size:6.2px}
.dk-client{left:32px;top:124px;font-size:9.4px;font-weight:700}
.dk-addr{left:32px;top:140px;font-size:5.9px}
.dk-contact{left:32px;top:150px;font-size:10px;font-weight:700}
.dk-box{position:absolute;left:19px;width:358px;top:178px;height:36px;background:var(--panel);border-radius:6px}
.dk-box__no{left:13px;top:6px;font-size:7.4px;font-weight:700}
.dk-box__text{left:13px;top:22px;font-size:4.9px}
.dk-panel{position:absolute;left:19px;width:358px;top:240px;height:218px;background:var(--panel);border-radius:6px}
.dk-pill{position:absolute;left:25px;top:230px;height:19px;padding:0 8px;border-radius:6px;background:var(--red);color:#fff;font-size:11px;font-weight:700;line-height:19px}
.dk-item{position:absolute;left:32px}
.dk-item__head{font-size:7.8px;font-weight:600;color:var(--orange-deep);line-height:10px}
.dk-item__desc{font-size:4.8px;line-height:7px}

/* certificate */
.cert{font-family:"Open Sans",sans-serif}
.cf{position:absolute;left:33px;font-size:8.6px;white-space:nowrap}
.cf b{font-weight:700}
.cf__val{position:absolute;left:53px;top:0}
.cert-num{color:var(--red);font-weight:700}
.cert-para{position:absolute;left:33px;width:340px;font-size:8.4px;line-height:14px}
.cert-sig{position:absolute;left:71px;top:404px;width:66px;height:24px;background:linear-gradient(90deg,#f4f4f4,#e8e8e8);border-radius:3px}
</style>
</head>
<body>

<!-- Cover -->
<section class="page page--cover">
  <div class="cover__brand">
    <div class="brand__name">VANTO3</div>
    <div class="brand__tag">PASSIVE FIRE PROTECTION</div>
  </div>
  <div class="cover__title">VANTO3</div>
  <div class="cover__sub">PROPOSAL</div>
  <div class="cover__pill">Passive fire protection specialists</div>
  <svg class="cover__art" viewBox="0 0 396 200" role="img" aria-label="Photograph of a high-rise building under construction with a tower crane against a blue sky">
    <defs>
      <linearGradient id="sky" x1="0" y1="0" x2="0" y2="1">
        <stop offset="0" stop-color="#3f7fd0"/>
        <stop offset=".55" stop-color="#a9c4e6"/>
        <stop offset="1" stop-color="#6d6f73"/>
      </linearGradient>
      <linearGradient id="arc" x1="0" y1="0" x2="1" y2="0">
        <stop offset="0" stop-color="#d21f32"/>
        <stop offset="1" stop-color="#f7941d"/>
      </linearGradient>
    </defs>
    <path d="M0 84 Q198 -30 396 84 L396 200 L0 200 Z" fill="url(#arc)"/>
    <path d="M0 90 Q198 -18 396 90 L396 200 L0 200 Z" fill="url(#sky)"/>
  </svg>
  <div class="cover__band">www.vanto3.com.au</div>
</section>

<!-- Quote -->
<section class="page page--quote">
  <div class="ghost-word">VANTO3</div>
  <div class="brand"><div class="brand__name">VANTO3</div><div class="brand__tag">PASSIVE FIRE PROTECTION</div></div>
  <div class="company">
    <div class="company__name">VANTO3 Pty Ltd</div>
    <div class="company__line">4/22 Calloway Street</div>
    <div class="company__line">Brindle VIC 3181</div>
    <div class="company__line">ABN: 48 602 915 774</div>
    <div class="company__line">admin@vanto3.com.au</div>
  </div>
  <div class="rule"></div>

  <div class="qtable__head">
    <span class="c-sl">SL.</span><span class="c-desc">Item Description</span><span class="c-price">Price</span><span class="c-qty">Qty.</span><span class="c-total">Total</span>
  </div>
  <div class="qtable__body">
    <div class="qrow" style="top:2px"><span class="c-sl">1</span><span class="c-desc">Lorem Ipsum Dolor</span><span class="c-price">$50.00</span><span class="c-qty">1</span><span class="c-total">$50.00</span></div>
    <div class="qrow" style="top:42px"><span class="c-sl">2</span><span class="c-desc">Pellentesque id neque ligula</span><span class="c-price">$20.00</span><span class="c-qty">3</span><span class="c-total">$60.00</span></div>
    <div class="qrow" style="top:82px"><span class="c-sl">3</span><span class="c-desc">Interdum et malesuada fames</span><span class="c-price">$10.00</span><span class="c-qty">2</span><span class="c-total">$20.00</span></div>
    <div class="qrow" style="top:122px"><span class="c-sl">4</span><span class="c-desc">Vivamus volutpat faucibus</span><span class="c-price">$90.00</span><span class="c-qty">1</span><span class="c-total">$90.00</span></div>
  </div>

  <div class="abs q-thanks">Thank you for your business</div>
  <div class="abs q-pay q-label-orange">Payment Info:</div>
  <div class="q-paygrid">
    <div><b>Account #:</b>1234 5678 9012</div>
    <div><b>A/C Name:</b>Lorem Ipsum</div>
    <div><b>Bank Details:</b>Add your details</div>
  </div>
  <div class="q-line"></div>
  <div class="abs q-terms q-label-orange">Terms &amp; Conditions</div>
  <p class="q-terms-text">Payment is due within fourteen days of invoice. Quoted prices remain valid for thirty days. Works outside scope are charged at standard rates.</p>

  <div class="q-sum" style="top:339px">Sub Total:<span>$220.00</span></div>
  <div class="q-sum" style="top:353px">Tax:<span>0.00%</span></div>
  <div class="q-sum q-sum--total" style="top:376px">Total:<span>$220.00</span></div>
  <div class="q-sign-line"></div>
  <div class="abs q-sign">Authorised Sign</div>
  <div class="url-pill">www.vanto3.com.au</div>
</section>

<!-- Work docket -->
<section class="page page--docket">
  <div class="ghost-word">VANTO3</div>
  <div class="brand"><div class="brand__name">VANTO3</div><div class="brand__tag">PASSIVE FIRE PROTECTION</div></div>
  <div class="company">
    <div class="company__name">VANTO3 Pty Ltd</div>
    <div class="company__line">4/22 Calloway Street</div>
    <div class="company__line">Brindle VIC 3181</div>
    <div class="company__line">ABN: 48 602 915 774</div>
    <div class="company__line">admin@vanto3.com.au</div>
  </div>
  <div class="rule"></div>

  <h1 class="abs dk-title">Work Docket</h1>
  <div class="abs dk-date">26th October, 2023</div>
  <div class="abs dk-client">Marlow Builders 148 Quarry</div>
  <div class="abs dk-addr">St Eastbank VIC 3209</div>
  <div class="abs dk-contact">Lorenzo</div>

  <div class="dk-box">
    <div class="abs dk-box__no">Work Docket: 1188</div>
    <div class="abs dk-box__text">Works completed at <b>31 Harlan Street, Westvale</b> as directed by <b>Lorenzo</b> of Marlow Builders as listed below.</div>
  </div>

  <div class="dk-panel"></div>
  <div class="dk-pill">Works Completed:</div>
  <div class="dk-item" style="top:254px"><div class="dk-item__head">Basement 1 – Fan Room</div><div class="dk-item__desc">1 x 20mm x 20mm penetration with conduit through blockwork wall (?)</div></div>
  <div class="dk-item" style="top:282px"><div class="dk-item__head">Basement 1 – Apartment 38 Garage</div><div class="dk-item__desc">2 x 100mm x 100mm penetration with sprinkler pipe &amp; wrap through slab wall (Wet Fire)</div></div>
  <div class="dk-item" style="top:310px"><div class="dk-item__head">Basement 1 – Apartment 34 Garage</div><div class="dk-item__desc">2 x 100mm x 100mm penetration with sprinkler pipe &amp; wrap through slab wall (Wet Fire)</div></div>
  <div class="dk-item" style="top:338px"><div class="dk-item__head">Basement 1 – Apartment 30 Garage</div><div class="dk-item__desc">2 x 100mm x 100mm penetration with sprinkler pipe &amp; wrap through slab wall (Wet Fire)</div></div>
  <div class="dk-item" style="top:366px"><div class="dk-item__head">Basement 1 – Apartment 28</div><div class="dk-item__desc">5mtrs of caulking through slab wall (one side only) (Brickies)</div></div>
  <div class="dk-item" style="top:397px"><div class="dk-item__head">Basement 1 – Apartment 28</div><div class="dk-item__desc">5mtrs of caulking through slab wall (one side only) (Brickies)</div></div>
  <div class="dk-item" style="top:428px"><div class="dk-item__head">Basement 1 – Back Stairwell</div><div class="dk-item__desc">1 x 400mm x 400mm penetration empty through blockwork wall (Builder)</div></div>
  <div class="url-pill">www.vanto3.com.au</div>
</section>

<!-- Certificate -->
<section class="page page--cert cert">
  <div class="ghost-word">VANTO3</div>
  <div class="brand"><div class="brand__name">VANTO3</div><div class="brand__tag">PASSIVE FIRE PROTECTION</div></div>
  <div class="company" style="font-family:'Montserrat',sans-serif">
    <div class="company__name">VANTO3 Pty Ltd</div>
    <div class="company__line">4/22 Calloway Street</div>
    <div class="company__line">Brindle VIC 3181</div>
    <div class="company__line">ABN: 48 602 915 774</div>
    <div class="company__line">admin@vanto3.com.au</div>
  </div>
  <div class="rule"></div>

  <div class="cf" style="top:130px"><b>Client:</b><span class="cf__val">Checkpoint Assess Pty Ltd</span></div>
  <div class="cf" style="top:151px"><b>Job:</b><span class="cf__val"><b>508 Ashgrove Road, Linden Hills</b></span></div>
  <div class="cf" style="top:173px"><b>Certificate Number:</b> <span class="cert-num">2324</span></div>
  <div class="cf" style="top:194px"><b>Reference:</b><span class="cf__val" style="white-space:normal;width:235px;line-height:12.5px">Fire/smoke sealing of your various service penetrations as detailed below.</span></div>

  <p class="cert-para" style="top:241px"><b>VANTO3 Pty. Ltd</b>. certifies that as part of our contracted works, we have carried out the above fire protection at <b>508 Ashgrove Road, Linden Hills</b> as instructed by <b>Mira Lane</b> of <b>Checkpoint Assess Pty Ltd.</b></p>
  <p class="cert-para" style="top:304px;line-height:12.5px">These works have been completed and checked using the approved proprietary fire resistance tested products &amp; systems as <b>per AS1530 part 4 &amp; AS4072 part 1</b></p>
  <p class="cert-para" style="top:341px;line-height:12.5px">Any works that are modified, damaged, or disturbed following completion are not covered by this certification.</p>
  <p class="cert-para" style="top:382px">Installed in accordance with the manufacturer’s specifications.</p>

  <div class="cf" style="top:412px"><b>Signed:</b></div>
  <div class="cert-sig" role="img" aria-label="Handwritten signature of the installer"></div>
  <div class="cf" style="top:433px"><b>Name:</b> Daniel Rooke</div>
  <div class="cf" style="top:454px"><b>Date:</b> 28<sup style="font-size:5px">th</sup> May, 2026</div>
  <div class="url-pill">www.vanto3.com.au</div>
</section>

</body>
</html>
```